【依頼の目的/概要】
電子書籍(pavlo)の表紙デザインをお願いします

【画像サイズ】
*RVSより抜粋
表紙ファイルの理想的な寸法は2,560×1,600ピクセルです。
注:画像の寸法は1,000×625ピクセル以上であることが必要です
画像の最大の寸法は10,000×10,000ピクセルです

【タイトル】
朝の庭で見つけた小さな灯りの話

サブキャッチ
~来場者2倍、満足度9割の老舗書店を育てた5つの習慣

【著者】
ミドリノタネ工房代表
組織進化コンサルタント
柳瀬 公平

【本の内容】
とても勤勉で勉強家の開業歯科医のみなさんが
がんばってもなかなか成果の出づらい分野、
「チーム創り」について。

まず互いを人として大事にすることで
スタッフが自然に結束し、
「ここで働けてよかった」
と思うようになる。
楽しいから自主的創造的に動くようになる。
すると成果の質も高くなる。
そうなるまでのステップを紹介。

著者はレポートを出す型のコンサルではなく、
現場に入り込んでゲーム性の高い体験型研修や
一人一人の話を聴いて言葉にならない本音を通訳することなどが得意。
愛と遊び心をもってプログラムを提供し伴走するので
笑顔が絶えることがない。

*参考資料として原稿を添付します

【デザイン要望】
特にイメージにこだわりはありませんので
自由な発想でのデザインご応募を楽しみにしています。

*次点、次々点の方への参加報酬を設定いたしました。

*その他、必要な情報がありましたらお問い合わせください。

スマホでpavloを見るとき、小さなアイコンが並ぶ中で最も目に留まるデザインで、
一目で重要なワードも目に入るデザインだったので採用させていただきました。

次点の二つについても同様の基準でしたが
色使いやフォントサイズなどを調整して、
もっとパッと目に入るものでしたら順序が変わったかもしれません。

特に、チームがテーマなので人の写真+見やすいデザインが両方だったらよりよかったかなと思います

皆さま、一所懸命やっていただいてありがとうございました。
こんなにもたくさんの方にご提案いただけてとてもうれしいです。
お礼を出せるのは3作品ですが
皆様にお礼を改めて申し上げたいと思います。

電子書籍の売れ行きにとても大事な表紙づくりのご協力、本当にありがとうございました。

```html
<!DOCTYPE html>
<html lang="ja">
<head>
<meta charset="utf-8">
<title>朝の庭で見つけた小さな灯りの話</title>
<link href="https://fonts.googleapis.com/css2?family=Noto+Sans+JP:wght@500;700;900&family=Noto+Serif+JP:wght@900&display=swap" rel="stylesheet">
<style>
  :root {
    --sky-top: #a9ddf5;
    --sky-bottom: #4aa6e2;
    --navy: #17346e;
    --ink: #111111;
    --accent: #1c84d6;
    --paper: #ffffff;
    --art-warm: #f3c9a8;
    --art-teal: #6fb9c7;
  }
  * { margin: 0; padding: 0; box-sizing: border-box; }
  html, body { width: 751px; height: 1200px; overflow: hidden; background: var(--paper); }
  .cover {
    position: relative; width: 751px; height: 1200px; overflow: hidden;
    font-family: "Noto Sans JP", sans-serif; color: var(--navy);
  }
  .hero {
    position: absolute; inset: 0 0 570px 0;
    background: linear-gradient(180deg, var(--sky-top) 0%, var(--sky-bottom) 100%);
  }
  .title { position: absolute; left: 38px; top: 26px; font-weight: 900; line-height: 1.3; }
  .title-line { display: block; font-size: 50px; letter-spacing: 1px; }
  .title-line.first { padding-bottom: 8px; border-bottom: 6px solid var(--paper); margin-bottom: 16px; }
  .title-line.second { font-size: 46px; }
  .author { position: absolute; left: 500px; top: 18px; font-weight: 700; }
  .author-role { font-size: 12px; line-height: 1.5; display: block; }
  .author-name { font-size: 28px; letter-spacing: 6px; display: block; margin-top: 4px; }
  .art-figures {
    position: absolute; left: 70px; top: 240px; width: 470px; height: 390px;
    background: linear-gradient(180deg, var(--art-warm) 0%, var(--art-teal) 100%);
    border-radius: 40px 40px 0 0; opacity: 0.9;
  }
  .art-motif {
    position: absolute; left: 520px; top: 110px; width: 231px; height: 470px;
    background: linear-gradient(180deg, rgba(255,255,255,0.55), rgba(255,255,255,0.15));
    border-radius: 90px 0 0 120px;
  }
  .lower { position: absolute; left: 0; right: 0; top: 630px; bottom: 0; background: var(--paper); color: var(--ink); }
  .bracket-note { position: absolute; left: 40px; top: 28px; width: 330px; height: 120px; }
  .bracket-note svg { position: absolute; inset: 0; }
  .bracket-text {
    position: absolute; inset: 0; display: flex; flex-direction: column; justify-content: center;
    align-items: center; font-weight: 900; font-size: 34px; line-height: 1.35;
  }
  .key-a { position: absolute; left: 385px; top: 0; font-weight: 900; font-size: 150px; line-height: 1; color: var(--accent); }
  .key-b { position: absolute; left: 0; right: 0; top: 150px; text-align: center; font-weight: 900; font-size: 190px; line-height: 1; letter-spacing: 40px; padding-left: 40px; }
  .link-word { position: absolute; left: 450px; top: 355px; font-weight: 900; font-size: 40px; }
  .steps {
    position: absolute; left: 0; right: 0; top: 400px; text-align: center;
    font-family: "Noto Serif JP", serif; font-weight: 900; color: var(--accent); line-height: 1;
  }
  .steps-num { font-size: 150px; }
  .steps-word { font-size: 96px; }
</style>
</head>
<body>
<main class="cover">
  <section class="hero">
    <div class="art-motif" role="img" aria-label="大きく淡い装飾モチーフ"></div>
    <div class="art-figures" role="img" aria-label="笑顔でガッツポーズをする二人のスタッフのイラスト"></div>
    <h1 class="title">
      <span class="title-line first">朝の庭で見つけた</span>
      <span class="title-line second">小さな灯りの話</span>
    </h1>
    <p class="author">
      <span class="author-role">ミドリノタネ工房代表</span>
      <span class="author-role">組織進化コンサルタント</span>
      <span class="author-name">柳瀬 公平</span>
    </p>
  </section>
  <section class="lower">
    <div class="bracket-note">
      <svg viewBox="0 0 330 120" width="330" height="120" aria-hidden="true">
        <path d="M30 6 L6 60 L30 114" fill="none" stroke="#111" stroke-width="5"/>
        <path d="M300 6 L324 60 L300 114" fill="none" stroke="#111" stroke-width="5"/>
      </svg>
      <p class="bracket-text"><span>来場者2倍、</span><span>満足度9割の</span></p>
    </div>
    <p class="key-a">老舗</p>
    <p class="key-b">書店</p>
    <p class="link-word">を育てた</p>
    <p class="steps"><span class="steps-num">5</span><span class="steps-word">つの習慣</span></p>
  </section>
</main>
</body>
</html>
```